Business Card for Yachting Management Company

Need a business card design for a new yachting project management company. Attached is the logo for the company.
Our clients are large yacht owners and captains.
Design must be in the style of the logo. Modern, elegant.

Example of data to show:
Oliver Tennant
Project Manager
(+34) 612 870 334
oliver@quarvel.net
Quarvel Management - Marisol Tower, Office 22 - NDR - Palma de Mallorca

The data above will have to be changed (by me) for the different people in the company over the next years.

Will be printed using CardHarbor (Lustrel Business Cards). They provide these guidelines for the size:
"the actual size of the card is 1050 x 600 pixels. However, the full bleed size is 1083 x 633 pixels, and the safe printing area is 1008 x 558 pixels."

```html
<!DOCTYPE html>
<html lang="en">
<head>
<meta charset="utf-8">
<title>Quarvel Management – Business Card</title>
<link rel="stylesheet" href="https://fonts.googleapis.com/css2?family=Montserrat:wght@400;500;700&display=swap">
<style>
  :root {
    --backdrop: #4a4a49;
    --card: #161616;
    --card-back: #111111;
    --brand-blue: #0f72bd;
    --text-light: #e9e9e9;
    --text-grey: #8a8a8a;
    --emboss: #232323;
  }
  * { box-sizing: border-box; margin: 0; padding: 0; }
  html, body {
    width: 1200px; height: 801px; overflow: hidden;
    background: var(--backdrop);
    font-family: "Montserrat", sans-serif;
  }
  .sheet {
    width: 1200px; height: 801px;
    display: flex; align-items: center; justify-content: center; gap: 40px;
  }
  .card {
    position: relative;
    width: 540px; height: 309px;
    border-radius: 16px;
    overflow: hidden;
    border-bottom: 3px solid var(--brand-blue);
    box-shadow: 0 14px 30px rgba(0,0,0,.35);
  }
  /* front */
  .card-front { background: var(--card); }
  .brand-name {
    position: absolute; left: 48px; top: 44px;
    color: var(--brand-blue);
    font-weight: 700; font-size: 44px; line-height: 1;
    letter-spacing: 1px;
  }
  .brand-sub {
    position: absolute; left: 50px; top: 96px;
    color: var(--brand-blue);
    font-weight: 700; font-size: 17px; letter-spacing: 9px;
  }
  .contact-row {
    position: absolute; left: 50px; top: 160px;
    display: flex; align-items: center; gap: 14px;
  }
  .person-name {
    color: var(--brand-blue); font-weight: 700; font-size: 22px;
    letter-spacing: .5px; text-transform: uppercase; line-height: 1.1;
  }
  .person-role { color: var(--text-light); font-size: 14px; margin-top: 4px; }
  .divider { width: 1.5px; height: 50px; background: var(--brand-blue); }
  .contact-list { list-style: none; color: var(--text-light); font-size: 13px; }
  .contact-list li { display: flex; align-items: center; gap: 8px; line-height: 22px; }
  .contact-list svg { width: 12px; height: 12px; fill: var(--brand-blue); }
  .address-band {
    position: absolute; left: 0; right: 0; bottom: 18px; height: 24px;
    background: var(--brand-blue);
    color: #fff; font-size: 12.5px;
    display: flex; align-items: center; padding-left: 48px;
  }
  /* back */
  .card-back {
    background: var(--card-back);
    display: flex; flex-direction: column; align-items: center; justify-content: center;
  }
  .back-name {
    color: var(--emboss); font-weight: 700; font-size: 64px; letter-spacing: 2px; line-height: 1;
  }
  .back-sub {
    color: var(--emboss); font-weight: 700; font-size: 22px; letter-spacing: 14px; margin-top: 14px;
  }
</style>
</head>
<body>
<main class="sheet">
  <section class="card card-front" aria-label="Card front">
    <div class="brand-name">Quarvel</div>
    <div class="brand-sub">MANAGEMENT</div>
    <div class="contact-row">
      <div class="person">
        <div class="person-name">Oliver Tennant</div>
        <div class="person-role">Project Manager</div>
      </div>
      <div class="divider"></div>
      <ul class="contact-list">
        <li>
          <svg viewBox="0 0 24 24" aria-hidden="true"><path d="M6.6 10.8a15.1 15.1 0 0 0 6.6 6.6l2.2-2.2c.3-.3.7-.4 1-.2 1.1.4 2.3.6 3.6.6.6 0 1 .4 1 1V20c0 .6-.4 1-1 1A17 17 0 0 1 3 4c0-.6.4-1 1-1h3.5c.6 0 1 .4 1 1 0 1.3.2 2.5.6 3.6.1.3 0 .7-.2 1z"/></svg>
          (+34) 612 870 334
        </li>
        <li>
          <svg viewBox="0 0 24 24" aria-hidden="true"><path d="M2 5h20v14H2zm2 2v.5l8 5 8-5V7l-8 5z"/></svg>
          oliver@quarvel.net
        </li>
      </ul>
    </div>
    <div class="address-band">Quarvel Management - Marisol Tower, Office 22 - NDR - Palma de Mallorca</div>
  </section>

  <section class="card card-back" aria-label="Card back">
    <div class="back-name">Quarvel</div>
    <div class="back-sub">MANAGEMENT</div>
  </section>
</main>
</body>
</html>
```